Visitenkarten-Design für architect i.a.
Aufgabenstellung
Logo ( Siehe Anhang)
scrinari
dessignader da construcziun aulta
maturitad professiunla
architect i.a.

```html
<!DOCTYPE html>
<html lang="de">
<head>
<meta charset="utf-8">
<title>Visitenkarte – torvel</title>
<link rel="stylesheet" href="https://fonts.googleapis.com/css2?family=Open+Sans:wght@400;600;700&display=swap">
<style>
  :root {
    --backdrop: #e9e7e4;
    --card-white: #ffffff;
    --card-slate: #4d6d79;
    --ink-slate: #46687a;
    --ink-logo: #4a5257;
    --accent-sky: #6cc3e6;
    --accent-deep: #3f5c68;
    --rule: #3a3a3a;
  }
  * { box-sizing: border-box; margin: 0; padding: 0; }
  html, body {
    width: 1200px; height: 963px; overflow: hidden;
    background: var(--backdrop);
    font-family: "Open Sans", Arial, sans-serif;
  }
  .stage { position: relative; width: 1200px; height: 963px; }

  .card { position: absolute; width: 535px; height: 346px; }
  .card--front { left: 319px; top: 95px; background: var(--card-white); }
  .card--back { left: 328px; top: 512px; background: var(--card-slate); }

  .brand { position: absolute; display: flex; align-items: center; font-weight: 700; }
  .brand__square { display: block; flex: none; }

  .card--front .brand { left: 40px; top: 140px; gap: 8px; color: var(--ink-logo); font-size: 36px; letter-spacing: 0.5px; }
  .card--front .brand__square { width: 20px; height: 20px; background: var(--accent-sky); }

  .card__divider { position: absolute; left: 241px; top: 23px; width: 1px; height: 301px; background: var(--rule); }

  .contact { position: absolute; left: 268px; top: 0; right: 10px; height: 100%; color: var(--ink-slate); }
  .contact__name { position: absolute; left: 2px; top: 40px; font-size: 26px; font-weight: 400; letter-spacing: 0.3px; }
  .contact__address { position: absolute; left: 2px; top: 98px; font-size: 11.5px; line-height: 15px; text-transform: uppercase; }
  .contact__row { position: absolute; left: 0; display: flex; align-items: center; gap: 9px; }
  .contact__row--phone { top: 218px; font-size: 15px; }
  .contact__row--mail { top: 275px; font-size: 9.5px; text-transform: uppercase; }
  .contact__icon { width: 36px; height: 36px; border-radius: 50%; display: flex; align-items: center; justify-content: center; flex: none; }
  .contact__icon--phone { background: var(--accent-sky); }
  .contact__icon--mail { background: var(--accent-deep); }

  .card--back .brand { left: 0; right: 0; top: 128px; justify-content: center; gap: 16px; color: #ffffff; font-size: 84px; line-height: 1; }
  .card--back .brand__square { width: 46px; height: 46px; background: #ffffff; }
</style>
</head>
<body>
<main class="stage">
  <section class="card card--front" aria-label="Vorderseite">
    <div class="brand">
      <span class="brand__square"></span>
      <span class="brand__name">torvel</span>
    </div>
    <div class="card__divider"></div>
    <div class="contact">
      <h1 class="contact__name">TORVELKINST</h1>
      <p class="contact__address">Torvel Urban Accommodation<br>Lindenrainweg 12 Photos:<br>6003 Kernau</p>
      <p class="contact__row contact__row--phone">
        <span class="contact__icon contact__icon--phone">
          <svg width="18" height="18" viewBox="0 0 24 24" aria-hidden="true"><path fill="#ffffff" d="M6.6 10.8a15.5 15.5 0 0 0 6.6 6.6l2.2-2.2c.3-.3.7-.4 1-.2 1.1.4 2.3.6 3.6.6.6 0 1 .4 1 1V20c0 .6-.4 1-1 1C10.6 21 3 13.4 3 4c0-.6.4-1 1-1h3.5c.6 0 1 .4 1 1 0 1.3.2 2.5.6 3.6.1.3 0 .7-.2 1z"/></svg>
        </span>
        <span>NAT. 079 412 07 56</span>
      </p>
      <p class="contact__row contact__row--mail">
        <span class="contact__icon contact__icon--mail">
          <svg width="18" height="14" viewBox="0 0 18 14" aria-hidden="true"><rect x="1" y="1" width="16" height="12" fill="none" stroke="#ffffff" stroke-width="1.6"/><path d="M1 1.5 9 8l8-6.5" fill="none" stroke="#ffffff" stroke-width="1.6"/></svg>
        </span>
        <span>torvelkinst@postfeld.ch</span>
      </p>
    </div>
  </section>

  <section class="card card--back" aria-label="Rückseite">
    <div class="brand">
      <span class="brand__square"></span>
      <span class="brand__name">torvel</span>
    </div>
  </section>
</main>
</body>
</html>
```